Design a Framework Graphic for Our Online VidStream Course

We have created a system/framework to help teach our students one of our main concepts. We teach content creators and business owners how to grow on VidStream.
We made a rough outline of how we'd like the framework to look. So we'd at least like this made into a better image, cleaned up and made more cohesive. But we're also interested in seeing other creative ways of visualizing the framework. It could be designed in several different ways. Most important things are showing the process of going through each of these steps, and then repeating it over and over again.
1. Reverse Engineering
2. Research
3. Record
4. Release
5. Rocket - this is the pinnacle moment and we want to emphasize it
6. Review - (it's wrong on the attached image)
7. Repeat
The original vision was to show the first 3 steps as "ramping" up to the release time, then the rocket visual, then the rest is done and it circles back to step 1.
We want it to be something our students could print out an put on their wall. Something memorable that will help them memorize the system.
We also need an icon that can represent each step. The icon doesn't necessarily have to be on the master framework graphic, but we need these icons for use in the rest of our materials. We'd like simple, black and white graphic icons that represent each step.
Use the color red in the photo and we can send you the "Clip Summit Institute" logo if you need.
Target Market(s)
Beginner to advanced content creators and business owners who want to learn how to grow on VidStream
Font styles to use
Other font styles liked:
- Helvetica Neue is our brand font
Look and feel

```html
<!DOCTYPE html>
<html lang="en">
<head>
<meta charset="utf-8">
<title>How to Grow – Clip Summit Institute Framework</title>
<link rel="stylesheet" href="https://fonts.googleapis.com/css2?family=Bebas+Neue&family=Inter:wght@600;700;800&display=swap">
<style>
  :root {
    --page-bg: #6d6d6d;
    --ink: #1e1e1e;
    --brand-red: #ed1c24;
    --paper: #eeeeee;
    --white: #ffffff;
    --step-1: #cccccc;
    --step-2: #d4b6b9;
    --step-3: #e9878e;
    --step-4: #f26b75;
    --step-5: #ee2a2f;
    --step-6: #a11a1e;
    --step-7: #7e1417;
    --return-grey: #bdbdbd;
  }
  html, body {
    margin: 0;
    padding: 0;
    width: 1200px;
    height: 1200px;
    overflow: hidden;
    background: var(--page-bg);
  }
  .framework-poster {
    position: absolute;
    left: 136px;
    top: 0;
    width: 928px;
    height: 1200px;
    display: block;
  }
  .title-text { font-family: "Bebas Neue", "Arial Narrow", sans-serif; fill: var(--white); }
  .brand-name { font-family: "Inter", Helvetica, Arial, sans-serif; font-weight: 700; fill: var(--white); }
  .step-label { font-family: "Inter", Helvetica, Arial, sans-serif; font-weight: 700; font-size: 15px; letter-spacing: 0.3px; }
  .step-label.dark { fill: #222222; }
  .step-label.light { fill: var(--white); }
  .step-badge circle { fill: var(--white); stroke: #444444; stroke-width: 2; }
  .step-badge text { font-family: "Inter", Helvetica, Arial, sans-serif; font-weight: 800; font-size: 19px; fill: #111111; text-anchor: middle; }
  .footer-url { font-family: "Inter", Helvetica, Arial, sans-serif; font-weight: 800; font-size: 23px; fill: var(--white); text-anchor: middle; }
</style>
</head>
<body>
<svg class="framework-poster" viewBox="0 0 866 1120" xmlns="http://www.w3.org/2000/svg" aria-label="How to grow framework: seven steps in a cycle">
  <defs>
    <linearGradient id="beam-fade" x1="0" y1="0" x2="0" y2="1">
      <stop offset="0" stop-color="#ee2a2f"/>
      <stop offset="1" stop-color="#ee2a2f" stop-opacity="0"/>
    </linearGradient>
    <linearGradient id="return-fade" gradientUnits="userSpaceOnUse" x1="596" y1="778" x2="325" y2="809">
      <stop offset="0" stop-color="#d81f26"/>
      <stop offset="1" stop-color="#bdbdbd"/>
    </linearGradient>
    <linearGradient id="sky-fade" x1="0" y1="0" x2="0" y2="1">
      <stop offset="0" stop-color="#cfe2ea"/>
      <stop offset="1" stop-color="#e6f2f6"/>
    </linearGradient>
    <linearGradient id="launch-tone" x1="0" y1="0" x2="0" y2="1">
      <stop offset="0" stop-color="#f1e4e4"/>
      <stop offset="0.6" stop-color="#f3d9d2"/>
      <stop offset="1" stop-color="#f1b49c"/>
    </linearGradient>
    <path id="star-shape" d="M0 -10 L2.65 -3.64 L9.51 -3.09 L4.28 1.39 L5.88 8.09 L0 4.5 L-5.88 8.09 L-4.28 1.39 L-9.51 -3.09 L-2.65 -3.64 Z"/>
    <marker id="cycle-head" viewBox="0 0 10 10" refX="5" refY="5" markerWidth="3.2" markerHeight="3.2" orient="auto">
      <path d="M0 0 L10 5 L0 10 Z" fill="#ffffff"/>
    </marker>
  </defs>

  <rect class="poster-paper" x="0" y="0" width="866" height="1120" fill="var(--paper)"/>

  <g class="poster-header">
    <rect x="0" y="0" width="866" height="152" fill="var(--ink)"/>
    <rect x="0" y="130" width="866" height="22" fill="var(--paper)"/>
    <polygon points="0,18 342,18 450,152 0,152" fill="var(--ink)"/>
    <polygon points="342,18 866,18 866,130 432,130" fill="var(--brand-red)"/>
    <rect x="0" y="0" width="866" height="18" fill="var(--brand-red)"/>
    <polygon points="687,90 866,90 866,152 642,152" fill="var(--ink)"/>

    <g class="brand-lockup">
      <rect x="44" y="48" width="78" height="78" fill="var(--brand-red)"/>
      <text class="brand-name" x="147" y="76" font-size="23">CLIP SUMMIT</text>
      <text class="brand-name" x="147" y="101" font-size="23">INSTITUTE</text>
    </g>

    <text class="title-text" x="632" y="80" font-size="72" text-anchor="middle" textLength="350" lengthAdjust="spacingAndGlyphs">HOW TO GROW ON</text>

    <g class="platform-name">
      <rect x="698" y="109" width="20" height="20" fill="var(--brand-red)"/>
      <text class="title-text" x="726" y="129" font-size="30">VIDSTREAM</text>
    </g>
  </g>

  <path class="cloud-bank" role="img" aria-label="Soft clouds illustration around the rocket launch" d="M0 1052 V855 Q210 830 420 858 Q620 720 866 560 V1052 Z" fill="url(#sky-fade)"/>

  <g class="step-ring">
    <path class="step-segment step-1" fill="var(--step-1)" d="M239.3 820.3 A336 336 0 0 1 112.4 648.8 L251.3 603.7 A190 190 0 0 0 323.0 700.6 Z"/>
    <path class="step-segment step-2" fill="var(--step-2)" d="M112.4 648.8 A336 336 0 0 1 103.4 475.1 L246.2 505.5 A190 190 0 0 0 251.3 603.7 Z"/>
    <path class="step-segment step-3" fill="var(--step-3)" d="M103.4 475.1 A336 336 0 0 1 182.3 320.2 L290.8 417.9 A190 190 0 0 0 246.2 505.5 Z"/>
    <path class="step-segment step-4" fill="var(--step-4)" d="M182.3 320.2 A336 336 0 0 1 333.8 223.7 L376.4 363.3 A190 190 0 0 0 290.8 417.9 Z"/>
    <path class="step-segment step-5" fill="var(--step-5)" d="M333.8 223.7 A336 336 0 0 1 530.2 223.7 L487.6 363.3 A190 190 0 0 0 376.4 363.3 Z"/>
    <path class="step-segment step-6" fill="var(--step-6)" d="M530.2 223.7 A336 336 0 0 1 689.4 329.0 L577.5 422.9 A190 190 0 0 0 487.6 363.3 Z"/>
    <path class="step-segment step-7" fill="var(--step-7)" d="M689.4 329.0 A336 336 0 0 1 764.7 498.2 L620.2 518.6 A190 190 0 0 0 577.5 422.9 Z"/>
    <polygon class="rocket-beam" points="376.4,363.3 487.6,363.3 446,482 418,482" fill="url(#beam-fade)"/>
  </g>

  <rect class="rocket-illustration" role="img" aria-label="Illustration of a red and white rocket lifting off with a flame trail into the clouds" x="362" y="482" width="140" height="550" fill="url(#launch-tone)"/>

  <g class="return-path" fill="none" stroke-width="5" stroke-linecap="round">
    <path d="M717 512 V578 A285 285 0 0 1 595.5 778.5" stroke="#c81e24"/>
    <path d="M595.5 778.5 A285 285 0 0 1 325.2 809.3" stroke="url(#return-fade)"/>
  </g>
  <polygon class="return-head" points="705,548 729,548 717,578" fill="#8f1518"/>
  <polygon class="return-head" points="583.9,786.5 611.6,780.6 599.0,762.6" fill="#d81f26"/>
  <polygon class="return-head" points="310.4,803.3 339.0,802.0 330.0,824.2" fill="var(--return-grey)"/>

  <g class="icon-reverse-engineering">
    <circle cx="212" cy="698" r="17" fill="none" stroke="#111" stroke-width="8" stroke-dasharray="6 7.35"/>
    <circle cx="212" cy="698" r="13" fill="#111"/>
    <circle cx="212" cy="698" r="5" fill="var(--step-1)"/>
    <path d="M186 686 A29 29 0 0 1 228 673" fill="none" stroke="#111" stroke-width="4"/>
    <path d="M238 710 A29 29 0 0 1 196 723" fill="none" stroke="#111" stroke-width="4"/>
  </g>
  <g class="icon-research">
    <circle cx="150" cy="558" r="21" fill="none" stroke="#111" stroke-width="7"/>
    <line x1="166" y1="575" x2="183" y2="593" stroke="#111" stroke-width="11" stroke-linecap="round"/>
  </g>
  <g class="icon-record">
    <circle cx="190" cy="430" r="34" fill="none" stroke="#111" stroke-width="4"/>
    <circle cx="190" cy="430" r="22" fill="none" stroke="#111" stroke-width="12"/>
  </g>
  <g class="icon-release" fill="none" stroke="#fff" stroke-width="4" stroke-linejoin="round">
    <path d="M254 319 L330 297 L302 353 L290 329 Z"/>
    <line x1="290" y1="329" x2="330" y2="297"/>
  </g>
  <g class="icon-rocket-growth">
    <rect x="400" y="273" width="12" height="22" fill="#fff"/>
    <rect x="416" y="263" width="12" height="32" fill="#fff"/>
    <rect x="432" y="253" width="12" height="42" fill="#fff"/>
    <path d="M392 291 L418 268 L436 276 L466 240" fill="none" stroke="#fff" stroke-width="6" stroke-linejoin="round" stroke-linecap="round"/>
    <polygon points="458,236 478,226 474,248" fill="#fff"/>
  </g>
  <g class="icon-review" fill="none" stroke="#fff" stroke-width="2.5">
    <use href="#star-shape" transform="translate(543 300)"/>
    <use href="#star-shape" transform="translate(567 300)"/>
    <use href="#star-shape" transform="translate(591 300)"/>
  </g>
  <g class="icon-repeat" fill="none" stroke="#fff" stroke-width="6">
    <path d="M693 414 A22 22 0 0 1 678.2 454.7" marker-end="url(#cycle-head)"/>
    <path d="M671 452.1 A22 22 0 0 1 685.8 411.3" marker-end="url(#cycle-head)"/>
  </g>

  <text class="step-label dark" transform="translate(258 772) rotate(-56)" text-anchor="middle">REVERSE
    <tspan x="0" dy="17">ENGINEERING</tspan></text>
  <text class="step-label dark" transform="translate(178 640) rotate(-20)" text-anchor="middle">RESEARCH</text>
  <text class="step-label dark" transform="translate(172 496) rotate(8)" text-anchor="middle">RECORD</text>
  <text class="step-label light" transform="translate(247 362) rotate(48)" text-anchor="middle">RELEASE</text>
  <text class="step-label light" x="432" y="342" text-anchor="middle">ROCKET</text>
  <text class="step-label light" transform="translate(622 368) rotate(-50)" text-anchor="middle">REVIEW</text>
  <text class="step-label light" transform="translate(702 494) rotate(-12)" text-anchor="middle">REPEAT</text>

  <g class="step-badge"><circle cx="162" cy="758" r="17"/><text x="162" y="765">1</text></g>
  <g class="step-badge"><circle cx="92" cy="585" r="17"/><text x="92" y="592">2</text></g>
  <g class="step-badge"><circle cx="125" cy="408" r="17"/><text x="125" y="415">3</text></g>
  <g class="step-badge"><circle cx="244" cy="267" r="17"/><text x="244" y="274">4</text></g>
  <g class="step-badge"><circle cx="431" cy="210" r="17"/><text x="431" y="217">5</text></g>
  <g class="step-badge"><circle cx="613" cy="265" r="17"/><text x="613" y="272">6</text></g>
  <g class="step-badge"><circle cx="739" cy="398" r="17"/><text x="739" y="405">7</text></g>

  <g class="poster-footer">
    <rect x="0" y="1052" width="866" height="6" fill="#111"/>
    <rect x="0" y="1058" width="866" height="62" fill="var(--brand-red)"/>
    <text class="footer-url" x="433" y="1098">WWW.CLIPSUMMITINSTITUTE.COM</text>
  </g>
</svg>
</body>
</html>
```